need 4 creative A frame (SANDWICH BOARD) designs concepts for dental office

need 4 creative A frame (SANDWICH BOARD) designs concepts
1 - targeting kids
2. targeting old age
3. targeting teens
4 targeting general public

website - www.brenvaxdental.ca

LINK for Measurements for sandwich board https://www.korvepa.ca/BL_1921/Aluminum-Snap-Edge-A-Frame-Sign

i am attaching certain key ingredients ( rough sketch in uploaded files ) to be added on each design though not mandatory if the design is very creative

```html
<!DOCTYPE html>
<html lang="en">
<head>
<meta charset="utf-8">
<title>Brenvax Dental – A-Frame Sign</title>
<link href="https://fonts.googleapis.com/css2?family=Montserrat:wght@600;700;800&family=Roboto:wght@900&display=swap" rel="stylesheet">
<style>
  :root {
    --navy: #14123a;
    --navy-deep: #0f0e30;
    --cyan: #00b4ec;
    --chevron-dim: #1e2850;
    --white: #ffffff;
    --page: #eef1f5;
  }
  * { margin: 0; padding: 0; box-sizing: border-box; }
  html, body {
    width: 1200px; height: 962px; overflow: hidden;
    background: var(--page);
    font-family: "Montserrat", sans-serif;
  }
  .sign {
    position: absolute; left: 247px; top: 31px;
    width: 706px; height: 900px;
    background: var(--navy);
    box-shadow: 0 6px 18px rgba(0,0,0,.18);
    overflow: hidden;
  }
  .hero {
    position: relative; height: 390px;
    background: linear-gradient(180deg, #f4f6f8 0%, #e3e6ea 35%, #c7b49a 70%, #6f7d96 100%);
  }
  .hero-photo {
    position: absolute; inset: 60px 0 0 0;
    background: linear-gradient(90deg, #c9a56e 0%, #5b7aa8 30%, #e9ecef 48%, #3f6ea8 62%, #9fd9c8 85%, #b8c6c9 100%);
    opacity: .85;
  }
  .headline {
    position: absolute; top: 20px; left: 0; right: 0;
    text-align: center; font-weight: 800; font-size: 34px;
    color: var(--navy); letter-spacing: .5px;
  }
  .rule {
    position: absolute; top: 402px; left: 0; right: 0;
    height: 3px; background: var(--cyan);
  }
  .brand-row {
    position: absolute; top: 418px; left: 0; right: 0; height: 160px;
  }
  .badge { position: absolute; top: 0; width: 156px; height: 156px; }
  .badge-open { left: 32px; }
  .badge-bill { right: 36px; }
  .brand-name {
    position: absolute; left: 190px; right: 190px; top: 56px;
    text-align: center; color: var(--white);
    font-weight: 700; font-size: 32px; line-height: 1.1;
  }
  .tagline {
    position: absolute; top: 578px; left: 0; right: 0;
    text-align: center; color: var(--white); font-weight: 800; font-size: 24px;
  }
  .chevrons { position: absolute; top: 634px; left: 0; width: 706px; height: 118px; }
  .accepting {
    position: absolute; top: 763px; left: 0; right: 0;
    text-align: center; color: var(--white); font-weight: 700; font-size: 30px;
  }
  .contact-bar {
    position: absolute; bottom: 0; left: 0; right: 0; height: 88px;
    background: var(--cyan);
    display: flex; align-items: center; justify-content: center; gap: 18px;
  }
  .phone-icon { width: 44px; height: 44px; }
  .phone-number { color: var(--navy); font-weight: 800; font-size: 56px; letter-spacing: 1px; }
</style>
</head>
<body>
  <main class="sign">
    <section class="hero">
      <div class="hero-photo" role="img" aria-label="Photo of a smiling multi-generation family: grandparents, parents and a young girl"></div>
      <h1 class="headline">CARE YOUR LOVE ONES</h1>
    </section>
    <div class="rule"></div>

    <section class="brand-row">
      <svg class="badge badge-open" viewBox="0 0 156 156" aria-label="Open 7 day">
        <circle cx="78" cy="78" r="76" fill="var(--cyan)" stroke="var(--cyan)" stroke-width="3" stroke-dasharray="4 3"/>
        <circle cx="78" cy="78" r="66" fill="none" stroke="var(--white)" stroke-width="3"/>
        <defs>
          <path id="arc-top" d="M30,78 A48,48 0 0 1 126,78"/>
          <path id="arc-bottom" d="M36,84 A42,42 0 0 0 120,84"/>
        </defs>
        <text font-family="Roboto, sans-serif" font-weight="900" font-size="22" fill="var(--navy)">
          <textPath href="#arc-top" startOffset="50%" text-anchor="middle">OPEN</textPath>
        </text>
        <text font-family="Roboto, sans-serif" font-weight="900" font-size="22" fill="var(--navy)">
          <textPath href="#arc-bottom" startOffset="50%" text-anchor="middle" dominant-baseline="hanging">DAY</textPath>
        </text>
        <text x="78" y="100" text-anchor="middle" font-family="Roboto, sans-serif" font-weight="900" font-size="58" fill="var(--navy)">7</text>
        <path d="M26,78 l3,-7 l3,7 l-6,-4 h6 z" fill="var(--navy)"/>
        <path d="M124,78 l3,-7 l3,7 l-6,-4 h6 z" fill="var(--navy)"/>
      </svg>

      <div class="brand-name">Brenvax Dental</div>

      <svg class="badge badge-bill" viewBox="0 0 156 156" aria-label="We direct bill">
        <circle cx="78" cy="78" r="76" fill="var(--cyan)"/>
        <circle cx="78" cy="78" r="66" fill="none" stroke="var(--white)" stroke-width="2.5" stroke-dasharray="0.1 7" stroke-linecap="round"/>
        <g font-family="Roboto, sans-serif" font-weight="900" font-size="25" fill="var(--navy)" text-anchor="middle">
          <text x="78" y="58">WE</text>
          <text x="78" y="86">DIRECT</text>
          <text x="78" y="114">BILL</text>
        </g>
      </svg>
    </section>

    <p class="tagline">WE’ RE IN</p>

    <svg class="chevrons" viewBox="0 0 706 118" aria-hidden="true">
      <defs>
        <path id="chevron" d="M59,0 h48 l-59,59 l59,59 h-48 l-59,-59 z"/>
      </defs>
      <use href="#chevron" x="75" fill="var(--chevron-dim)"/>
      <use href="#chevron" x="163" fill="var(--chevron-dim)"/>
      <use href="#chevron" x="251" fill="var(--cyan)"/>
      <use href="#chevron" x="339" fill="var(--cyan)"/>
      <use href="#chevron" x="427" fill="var(--chevron-dim)"/>
      <use href="#chevron" x="515" fill="var(--chevron-dim)"/>
    </svg>

    <p class="accepting">Accepting New Patients</p>

    <footer class="contact-bar">
      <svg class="phone-icon" viewBox="0 0 24 24" aria-hidden="true">
        <path fill="var(--navy)" d="M6.6 10.8c1.4 2.8 3.8 5.1 6.6 6.6l2.2-2.2c.3-.3.7-.4 1-.2 1.1.4 2.3.6 3.6.6.6 0 1 .4 1 1V20c0 .6-.4 1-1 1C10.6 21 3 13.4 3 4c0-.6.4-1 1-1h3.5c.6 0 1 .4 1 1 0 1.3.2 2.5.6 3.6.1.3 0 .7-.2 1z"/>
        <path fill="none" stroke="var(--navy)" stroke-width="1.8" stroke-linecap="round" d="M14 3.5a7 7 0 0 1 6.5 6.5M14 7a3.5 3.5 0 0 1 3 3"/>
      </svg>
      <span class="phone-number">587 555 0142</span>
    </footer>
  </main>
</body>
</html>
```